Looking for an Innovative Print Design (Service Directory)

We need a new design for our advertisement within a printed colour services directory.

We are a compensation law firm called Velbrook Compensation Lawyers. Feel free to take a browse of our website www.velbrooklegal.com.au to get an idea of what we do and the kind of firm we are.

We are in the process of redeveloping our website and as such, so please don't adhere to the design principles of the current site- impress us with your originality!

On top of any editable formats, your final submissions must include a .pdf copy.
The same design will need to be presented in two dimensions:

- 154mm x 118mm (B1/B2 Half Page);
- 175mm x 113mm (B4 Half Page).

[For more information refer to attached Pdf.]

We have attached for you a few examples of other firms' designs (Sample1,2,3). These are by no means good, or what we're after, it's just to provide you with an idea of what sort of advertisements go into the service directory.

Hi all,

We want to emphasise that a priority of the design is that it must look:
• Professional
• Sophisticated
Please do not hesitate to use completely different colour schemes to the ones that are on our website- as we have said, our website will change in the near future, so cohesion between the current project and the website is not necessary!

Thanks!

Thank you for your submissions so far. There are some great ideas hidden in there. 

An issue we are having is that most of you are conforming to the same understanding of what it should look like. Remember that there is NO NEED to be bound by the image of firm as is. That is, feel free to use a different colour logo.

For inspiration, we relate well to the design aesthetics of: http://www.tinfernstudio.co.uk/

Look forward to seeing your 'out of the box' submissions. 

Reason: We've received a large amount of fantastic designs. However, what we're really looking for is something original. Please feel free to think outside the box (the final design doesn't need to look like a print ad), and construct a design that is completely incongruous with our website! While we do appreciate a minimalistic design, we have yet to receive something that really grabs your attention with its visuals. We're not sure but this may or may not be achieved with a full colour design. Thanks for all your submissions- they all have some features that really click with us. We look forward to the next wave of submissions!

Target Market(s)

We have various target markets, including mainly families, elderly people, blue collar workers.

These are individuals who are looking for assistance. They feel helpless or wronged.

Keep in mind that the people accessing these are those who prefer going to a printed directory rather than using a google search.

Industry/Entity Type

Law Firm

Font styles to use
Serif
Sans Serif

Requirements
Must have
• - Our name 'Velbrook Compensation Lawyers'
- Our logo (attached as logo.eps, logo.png, and logo.tif)
- Must include phone number as 1300 XXX XXX (this must be prominent)
- Must include the following service areas in these words: Motor vehicle claims, medical claims, superannuation claims, Workplace claims, negligence claims
- Our email address: info@velbrooklegal.com.au
- Our website address: www.velbrooklegal.com.au
- The following catchphrases: '98% success rate', and 'No win no fee' in those words
- Our location '412 Carvel Lane, Smithville, SYDNEY'
- For sizing dimensions, we need one in 154mm x 118mm and also a design in 175mm x 113mm (B4 Half Page) [refer to pdf attached]
Nice to have
• - Text indicating free initial consulatation
- Professional colour scheme
- As our website will be changed, do not worry about making the advertisement cohesive with our website design
- We want the design to be modern, but still professional
- Clean typeface
- No gradient colour scheme
- When designing, if you are looking to place more text onto the advertisement, these may be some considerations (feel free to change the wording): Accredited specialists, home and hospital visits

```html
<!DOCTYPE html>
<html lang="en">
<head>
<meta charset="utf-8">
<title>Velbrook Compensation Lawyers – Directory Advertisement</title>
<link rel="stylesheet" href="https://fonts.googleapis.com/css2?family=Source+Sans+3:wght@600;800&family=Roboto+Condensed:wght@400;700&family=EB+Garamond:wght@400&display=swap">
<style>
  :root {
    --page: #ffffff;
    --panel: #000000;
    --gold: #f7b918;
    --white: #ffffff;
    --ink: #1a1a1a;
    --photo-a: #6f6e6c;
    --photo-b: #c9c9c7;
    --photo-c: #3c3d40;
  }
  * { margin: 0; padding: 0; box-sizing: border-box; }
  html, body { width: 1200px; height: 1000px; overflow: hidden; background: var(--page); }
  .canvas { position: relative; width: 1200px; height: 1000px; }

  .ad { position: absolute; background: var(--panel); overflow: hidden; font-family: "Source Sans 3", Arial, sans-serif; }
  .ad--half-b1 { left: 275px; top: 0; width: 652px; height: 500px; }
  .ad--half-b4 { left: 214px; top: 500px; width: 774px; height: 500px; }

  .ad__photo { position: absolute; left: 0; top: 0; width: 100%;
    background: linear-gradient(100deg, var(--photo-a) 0%, var(--photo-b) 30%, var(--photo-b) 62%, var(--photo-c) 78%, var(--photo-a) 100%); }
  .ad--half-b1 .ad__photo { height: 262px; }
  .ad--half-b4 .ad__photo { height: 240px; }

  .ad__headline, .ad__phone { position: absolute; left: 0; width: 100%; text-align: center; color: var(--gold);
    font-weight: 800; line-height: 1; text-shadow: 3px 3px 3px rgba(0,0,0,.75); white-space: nowrap; }
  .ad--half-b1 .ad__headline { top: 10px; font-size: 54px; }
  .ad--half-b4 .ad__headline { top: 10px; font-size: 57px; }
  .ad--half-b1 .ad__phone { top: 190px; font-size: 72px; }
  .ad--half-b4 .ad__phone { top: 166px; font-size: 75px; }

  .ad__badge { position: absolute; border-radius: 50%; background: var(--gold); border: 4px solid var(--white);
    box-shadow: 2px 3px 6px rgba(0,0,0,.5); display: flex; align-items: center; justify-content: center; text-align: center;
    font-family: "Roboto Condensed", Arial, sans-serif; font-weight: 700; color: var(--ink); line-height: 1; }
  .ad--half-b1 .ad__badge { left: 14px; top: 47px; width: 112px; height: 112px; font-size: 29px; }
  .ad--half-b4 .ad__badge { left: 28px; top: 45px; width: 116px; height: 116px; font-size: 31px; }

  .ad__firm { position: absolute; left: 0; width: 100%; text-align: center; color: var(--white);
    font-family: "EB Garamond", Georgia, serif; font-weight: 400; line-height: 1; white-space: nowrap; }
  .ad--half-b1 .ad__firm { top: 264px; font-size: 38px; letter-spacing: 1.6px; }
  .ad--half-b4 .ad__firm { top: 243px; font-size: 41px; letter-spacing: 1.6px; }

  .ad__services { position: absolute; list-style: none; color: var(--gold); font-weight: 600; }
  .ad__services li::before { content: "•"; display: inline-block; width: 22px; }
  .ad--half-b1 .ad__services { left: 12px; top: 314px; font-size: 26px; line-height: 27px; }
  .ad--half-b4 .ad__services { left: 12px; top: 784px; top: 284px; font-size: 28px; line-height: 28px; }

  .ad__contact { position: absolute; color: var(--white); font-family: "Roboto Condensed", Arial, sans-serif; }
  .ad--half-b1 .ad__contact { left: 339px; top: 310px; font-size: 28px; line-height: 33px; }
  .ad--half-b4 .ad__contact { left: 424px; top: 282px; font-size: 29px; line-height: 36px; }

  .ad__brand { position: absolute; color: var(--white); font-weight: 600; line-height: 1; white-space: nowrap; }
  .ad--half-b1 .ad__brand { left: 350px; top: 394px; font-size: 46px; }
  .ad--half-b4 .ad__brand { left: 432px; top: 384px; font-size: 50px; }

  .ad__offer { position: absolute; color: var(--white); font-family: "Roboto Condensed", Arial, sans-serif; font-weight: 700; white-space: nowrap; }
  .ad--half-b1 .ad__offer { left: 45px; top: 458px; font-size: 20px; }
  .ad--half-b4 .ad__offer { left: 71px; top: 456px; font-size: 21px; }

  .ad__address { position: absolute; color: var(--white); font-family: "EB Garamond", Georgia, serif; white-space: nowrap; }
  .ad--half-b1 .ad__address { left: 351px; top: 461px; font-size: 17px; letter-spacing: 0.4px; }
  .ad--half-b4 .ad__address { left: 428px; top: 460px; font-size: 18px; letter-spacing: 0.4px; }
</style>
</head>
<body>
<main class="canvas">
  <section class="ad ad--half-b1">
    <div class="ad__photo" role="img" aria-label="Photo of a denied insurance claim form stamped in red beside a smartphone on a call screen"></div>
    <p class="ad__headline">98% SUCESS RATE</p>
    <div class="ad__badge">NO WIN<br>NO FEE</div>
    <p class="ad__phone">1300 xxx xxxx</p>
    <h1 class="ad__firm">Velbrook Compensation Lawyers</h1>
    <ul class="ad__services">
      <li>Motor vehicle claims</li>
      <li>Medical claims</li>
      <li>Superannuation claims</li>
      <li>Workplace claims</li>
      <li>Negligence claims</li>
    </ul>
    <div class="ad__contact">
      <p>www.velbrooklegal.com.au</p>
      <p>info@velbrooklegal.com.au</p>
    </div>
    <p class="ad__brand">Velbrook</p>
    <p class="ad__offer">FREE INITIAL CONSULTATION</p>
    <p class="ad__address">412 Carvel Lane, Smithville, SYDNEY</p>
  </section>

  <section class="ad ad--half-b4">
    <div class="ad__photo" role="img" aria-label="Photo of a denied insurance claim form stamped in red beside a smartphone on a call screen"></div>
    <p class="ad__headline">98% SUCESS RATE</p>
    <div class="ad__badge">NO WIN<br>NO FEE</div>
    <p class="ad__phone">1300 xxx xxxx</p>
    <h1 class="ad__firm">Velbrook Compensation Lawyers</h1>
    <ul class="ad__services">
      <li>Motor vehicle claims</li>
      <li>Medical claims</li>
      <li>Superannuation claims</li>
      <li>Workplace claims</li>
      <li>Negligence claims</li>
    </ul>
    <div class="ad__contact">
      <p>www.velbrooklegal.com.au</p>
      <p>info@velbrooklegal.com.au</p>
    </div>
    <p class="ad__brand">Velbrook</p>
    <p class="ad__offer">FREE INITIAL CONSULTATION</p>
    <p class="ad__address">412 Carvel Lane, Smithville, SYDNEY</p>
  </section>
</main>
</body>
</html>
```